Pizza Coupon App Design Project

*******This project will have a guaranteed payout once I see that there is quality work being designed*********

I require the design (no coding) of 4 vertical screens (the screen will not change for horizontal orientation) for Zelvo and Quembra. The highest res should be used so it can be scaled for older generation phones.

The mobile app will be used to access pizza coupons.

I do not have a specific style or look that I am going for, although I do not want a childish design (e.g. comic sans). The main requirements are for it to be very easy for users to understand and navigate and to be clean and professional.

I am happy if you only produce a design of the main and store selection screens to which I will give feedback before continuing to design the remaining screens.

The selected artist must be flexible in adapting the final design slightly after the contest is completed, during the app development process (maybe a few small modifications over a month or so).
Please do not include any copyrighted images in your deliverables. I must be the sole owner of the graphics once I have paid for them.

I have included attachments which show the process flow and the screen requirements so that will give you the detail you need to design them. I have also included the logo to assist you in your design., *******This project is now guaranteed *********

I have included attachments which show the process flow and the screen requirements so that will give you the detail you need to design them. I have also included the logo to assist you in your design., *******This project will have a guaranteed payout once I see that there is quality work being designed*********

I have included attachments which show the process flow and the screen requirements so that will give you the detail you need to design them. I have also included the logo to assist you in your design.

Updates

Reason: Still looking for the perfect design! ******Project is now guaranteed******

******Project is now guaranteed******

Reason: Starting to get some great designs, we are getting much closer! Keep it up.

Target Market(s)

students and 18-30 year olds - People who want cheap meals and people who order pizza online., students and 18-30 year olds - People who want cheap meals and people who order pizza online., students and 18-30 year olds - People who want cheap meals and people who order pizza online.

Industry/Entity Type

Store

Requirements
Must have
• Must have requirements are listed in the attached documents., Must have requirements are listed in the attached documents., Must have requirements are listed in the attached documents.

```html
<!DOCTYPE html>
<html lang="en">
<head>
<meta charset="utf-8">
<title>Select Your Store</title>
<link rel="stylesheet" href="https://fonts.googleapis.com/css2?family=Arimo:wght@400;700&family=Roboto+Condensed:wght@700&display=swap">
<style>
  :root{
    --page:#e9e6e2;
    --wood-light:#7a5636;
    --wood-mid:#4e321d;
    --header-light:#c49a6c;
    --header-mid:#a97d52;
    --ink:#f3ece4;
    --ink-soft:#d9cfc4;
    --accent:#e3241b;
    --header-ink:#1a1009;
    --search-bg:#2a1b10;
    --search-line:#8b6a4c;
    --divider:rgba(0,0,0,.45);
    --pizza-crust:#e3a93b;
    --pizza-sauce:#b8541f;
  }
  *{box-sizing:border-box;margin:0;padding:0}
  html,body{width:1200px;height:1040px;overflow:hidden}
  body{background:var(--page);font-family:"Arimo",Arial,sans-serif;position:relative}

  .screen{
    position:absolute;left:320px;top:23px;width:560px;height:994px;overflow:hidden;
    background:
      radial-gradient(ellipse 70% 60% at 50% 45%, rgba(0,0,0,0) 40%, rgba(0,0,0,.75) 100%),
      linear-gradient(90deg,var(--wood-mid),var(--wood-light) 30%,var(--wood-mid) 55%,var(--wood-light) 80%,var(--wood-mid));
    box-shadow:0 20px 50px rgba(0,0,0,.25);
  }
  .planks{position:absolute;inset:0;pointer-events:none;z-index:1}

  .status-bar{
    position:relative;z-index:2;height:32px;background:rgba(0,0,0,.55);
    display:flex;align-items:center;justify-content:space-between;padding:0 12px;
    color:var(--ink);font-size:15px;font-weight:700;
  }
  .status-bar .carrier{display:flex;align-items:center;gap:6px}
  .status-bar .time{position:absolute;left:0;right:0;text-align:center}
  .status-bar .battery{display:flex;align-items:center}

  .store-header{
    position:relative;height:112px;margin:0 10px;padding:36px 0 0 20px;
    background:linear-gradient(180deg,var(--header-light),var(--header-mid));
    box-shadow:inset 0 -2px 6px rgba(0,0,0,.25);
  }
  .store-header h1{
    position:relative;z-index:2;
    font-family:"Roboto Condensed","Arial Narrow",sans-serif;
    font-size:30px;font-weight:700;color:var(--header-ink);letter-spacing:-.2px;
    text-shadow:0 1px 0 rgba(255,235,210,.5);
  }

  .search{
    position:relative;z-index:2;margin:24px 24px 0;height:50px;border-radius:25px;
    background:var(--search-bg);border:2px solid var(--search-line);
    display:flex;align-items:center;padding:0 14px;gap:10px;
    color:var(--ink);font-size:22px;
  }
  .search .query{flex:1}
  .search .caret{display:inline-block;width:2px;height:24px;background:var(--ink);vertical-align:middle;margin-left:1px}

  .store-list{position:relative;z-index:2;list-style:none;margin-top:36px}
  .store{
    display:flex;align-items:flex-start;height:138px;padding:14px 0 0 25px;
    border-top:2px solid var(--divider);
  }
  .store:first-child{border-top:none}
  .store-photo{
    width:140px;height:88px;flex:none;margin-top:6px;border-radius:50%;
    background:radial-gradient(circle at 45% 45%,var(--pizza-crust) 0 30%,var(--pizza-sauce) 60%,var(--pizza-crust) 66%,rgba(0,0,0,0) 70%);
  }
  .store-info{margin-left:18px}
  .store-name{font-size:30px;color:var(--ink);line-height:1.1;letter-spacing:-.3px;white-space:nowrap}
  .store-name mark{background:none;color:var(--accent)}
  .store-detail{font-size:13px;font-weight:700;color:var(--ink-soft);line-height:1.6;margin-top:6px}
  .store-hours{font-size:13px;color:var(--ink-soft);line-height:1.6}
  .store-hours b{font-weight:700;color:var(--ink)}
</style>
</head>
<body>
<main class="screen">
  <svg class="planks" width="560" height="994" aria-hidden="true">
    <g stroke="rgba(0,0,0,.3)" stroke-width="2">
      <line x1="70" y1="32" x2="70" y2="994"/><line x1="140" y1="32" x2="140" y2="994"/>
      <line x1="210" y1="32" x2="210" y2="994"/><line x1="280" y1="32" x2="280" y2="994"/>
      <line x1="350" y1="32" x2="350" y2="994"/><line x1="420" y1="32" x2="420" y2="994"/>
      <line x1="490" y1="32" x2="490" y2="994"/>
    </g>
  </svg>

  <div class="status-bar">
    <span class="carrier">
      <svg width="22" height="12" aria-hidden="true"><g fill="#f3ece4"><rect x="0" y="8" width="3" height="4"/><rect x="5" y="6" width="3" height="6"/><rect x="10" y="4" width="3" height="8"/><rect x="15" y="2" width="3" height="10"/></g></svg>
      Vantel
    </span>
    <span class="time">4:20 PM</span>
    <span class="battery">
      <svg width="34" height="16" aria-hidden="true"><rect x="1" y="1" width="28" height="14" rx="2" fill="none" stroke="#f3ece4" stroke-width="2"/><rect x="4" y="4" width="22" height="8" fill="#f3ece4"/><rect x="30" y="5" width="3" height="6" fill="#f3ece4"/></svg>
    </span>
  </div>

  <header class="store-header"><h1>Select Your Store</h1></header>

  <div class="search">
    <svg width="20" height="20" aria-hidden="true"><circle cx="8" cy="8" r="6" fill="none" stroke="#f3ece4" stroke-width="2"/><line x1="12.5" y1="12.5" x2="18" y2="18" stroke="#f3ece4" stroke-width="2.5"/></svg>
    <span class="query">Pizza Pa<span class="caret"></span></span>
    <svg width="22" height="22" aria-hidden="true"><circle cx="11" cy="11" r="10" fill="#8b6a4c"/><path d="M7 7l8 8M15 7l-8 8" stroke="#2a1b10" stroke-width="2"/></svg>
  </div>

  <ul class="store-list">
    <li class="store">
      <div class="store-photo" role="img" aria-label="Pizza slices photo"></div>
      <div class="store-info">
        <p class="store-name"><mark>Pizza Pa</mark>rlor</p>
        <p class="store-detail">Larch Avenue | Pine Hollow<br>WI 54000 | 715-555-0142</p>
        <p class="store-hours"><b>OPEN DAILY</b> 11am - 10pm</p>
      </div>
    </li>
    <li class="store">
      <div class="store-photo" role="img" aria-label="Pizza slices photo"></div>
      <div class="store-info">
        <p class="store-name"><mark>Pizza</mark> &amp; <mark>Pa</mark>sta delight</p>
        <p class="store-detail">48 Carden St. | Lakeview<br>NY 10000 | (212) 555-0187</p>
        <p class="store-hours"><b>OPEN DAILY</b> 11am - 10pm</p>
      </div>
    </li>
    <li class="store">
      <div class="store-photo" role="img" aria-label="Pizza slices photo"></div>
      <div class="store-info">
        <p class="store-name"><mark>Pizza Pa</mark>rlor</p>
        <p class="store-detail">Larch Avenue | Pine Hollow<br>WI 54000 | 715-555-0142</p>
        <p class="store-hours"><b>OPEN DAILY</b> 11am - 10pm</p>
      </div>
    </li>
    <li class="store">
      <div class="store-photo" role="img" aria-label="Pizza slices photo"></div>
      <div class="store-info">
        <p class="store-name"><mark>Pizza</mark> &amp; <mark>Pa</mark>sta delight</p>
        <p class="store-detail">48 Carden St. | Lakeview<br>NY 10000 | (212) 555-0187</p>
        <p class="store-hours"><b>OPEN DAILY</b> 11am - 10pm</p>
      </div>
    </li>
    <li class="store">
      <div class="store-photo" role="img" aria-label="Pizza slices photo"></div>
      <div class="store-info">
        <p class="store-name"><mark>Pizza Pa</mark>rlor</p>
        <p class="store-detail">Larch Avenue | Pine Hollow<br>WI 54000 | 715-555-0142</p>
        <p class="store-hours"><b>OPEN DAILY</b> 11am - 10pm</p>
      </div>
    </li>
    <li class="store">
      <div class="store-photo" role="img" aria-label="Pizza slices photo"></div>
      <div class="store-info">
        <p class="store-name"><mark>Pizza</mark> &amp; <mark>Pa</mark>sta delight</p>
        <p class="store-detail">48 Carden St. | Lakeview<br>NY 10000 | (212) 555-0187</p>
        <p class="store-hours"><b>OPEN DAILY</b> 11am - 10pm</p>
      </div>
    </li>
  </ul>
</main>
</body>
</html>
```